Design WORDPRESS Website for E Commerce Business

We are needing a WORDPRESS website for an E Commerce Business that is supplying quailty kids / baby products.

Target Market(s)

Female / Working Mums / New Mums

Industry/Entity Type

Business

Number of Pages Required

1 page

Font styles to use
Sans Serif

Colors
33b8a4
f8fcfd
d3a5cc
f7f1f7
cbcbcb
9d9d9d

```html
<!DOCTYPE html>
<html lang="en">
<head>
<meta charset="utf-8">
<title>Little Burrow – Quality Kids &amp; Baby Products</title>
<link href="https://fonts.googleapis.com/css2?family=Arimo:wght@400;700&family=Lora:ital,wght@1,600&display=swap" rel="stylesheet">
<style>
:root{
  --teal:#33b8a4;
  --teal-dark:#2c7b73;
  --teal-nav:#317f77;
  --blue:#3a8ea8;
  --blue-deep:#0d5f8f;
  --sky:#8fdcf5;
  --ink:#2a2a2a;
  --text:#555;
  --grey:#9d9d9d;
  --grey-light:#cbcbcb;
  --bg:#f8fcfd;
  --white:#fff;
  --footer-a:#0b1f2c;
  --footer-b:#0f5a8a;
  --ring:#a8dcef;
}
*{box-sizing:border-box;margin:0;padding:0}
html,body{width:1200px;height:3352px;overflow:hidden}
body{position:relative;background:var(--white);font-family:"Arimo",Arial,sans-serif;color:var(--text)}
.abs{position:absolute}
a{color:inherit;text-decoration:none}

/* header */
.site-header{position:absolute;left:0;top:0;width:1200px;height:92px;background:var(--white)}
.brand{left:161px;top:18px;display:flex;align-items:center;gap:12px}
.brand-dot{width:40px;height:40px;border-radius:50%;background:var(--grey)}
.brand-name{font-size:26px;font-weight:700;color:var(--teal);line-height:1}
.brand-rule{left:161px;top:0;width:134px;height:4px;background:var(--teal)}
.info-box{top:16px;height:60px;display:flex;align-items:center;gap:10px;padding:0 16px;color:var(--white);font-size:11px;line-height:1.4}
.info-address{left:686px;width:150px;background:#8a8a8a}
.info-call{left:887px;width:150px;background:var(--teal)}
.info-call strong{font-size:13px}

/* nav */
.main-nav{left:0;top:92px;width:1200px;height:49px;background:var(--teal-nav);border-bottom:3px solid var(--teal)}
.nav-links{position:absolute;left:161px;top:0;height:46px;display:flex;align-items:center;gap:31px;list-style:none;color:var(--white);font-size:11.5px}
.nav-search{position:absolute;left:836px;top:12px;width:201px;height:24px;background:var(--white);border-radius:2px;font-size:10px;color:#aaa;padding:6px 10px}
.nav-search span{position:absolute;right:0;top:0;width:24px;height:24px;background:var(--grey-light)}

/* hero */
.hero{left:0;top:141px;width:1200px;height:467px;background:linear-gradient(110deg,#b89a8a 0%,#d9b7a3 30%,#c77a8e 60%,#9c3a5c 85%,#7a2d48 100%)}
.hero-panel{left:387px;top:315px;width:424px;height:157px;background:rgba(60,60,60,.72);text-align:center;color:var(--white)}
.hero-kicker{margin-top:36px;font-size:12.5px;font-weight:700}
.hero-title{margin-top:10px;font-size:26px;letter-spacing:.5px}
.hero-btn{display:inline-block;margin-top:12px;width:128px;height:30px;line-height:30px;background:var(--teal);font-size:11px}

/* welcome */
.welcome-title{left:0;top:685px;width:1200px;text-align:center;font-family:"Lora",Georgia,serif;font-style:italic;font-weight:600;font-size:29px;color:var(--teal)}
.welcome-text{left:239px;top:748px;width:722px;text-align:center;font-size:14.5px;line-height:25px;color:var(--text)}
.pill-btn{height:31px;line-height:31px;text-align:center;color:var(--white);background:var(--blue);border-radius:16px;font-size:11px}
.welcome-btn{left:536px;top:874px;width:128px}

/* services */
.section-title{left:0;width:1200px;text-align:center;font-size:28px;letter-spacing:.5px;color:var(--ink)}
.section-title em{font-style:normal;color:var(--teal)}
.services-title{top:1006px}
.services-sub{left:0;top:1056px;width:1200px;text-align:center;font-size:16px;color:var(--text)}
.service{width:330px;text-align:center}
.service-photo{width:219px;height:219px;margin:0 auto;border-radius:50%;border:4px solid var(--ring)}
.service-name{margin-top:24px;font-size:11px;color:var(--teal);letter-spacing:.3px}
.service-text{margin-top:8px;font-size:11px;line-height:17px;color:#444}
.service-more{display:inline-block;margin-top:12px;font-size:9.5px;color:var(--teal);border-bottom:1px solid var(--teal)}
.tone-a{background:linear-gradient(135deg,#d8d3cc,#a86f5c)}
.tone-b{background:linear-gradient(135deg,#e7b58c,#d9665c)}
.tone-c{background:linear-gradient(135deg,#f0ece6,#a77b52)}
.tone-d{background:linear-gradient(135deg,#f3ede8,#b98354)}
.tone-e{background:linear-gradient(135deg,#f4f4f4,#d8b449)}
.tone-f{background:linear-gradient(135deg,#efe9e4,#8f5f4f)}

/* products */
.products{left:0;top:1967px;width:1200px;height:487px;background:linear-gradient(90deg,var(--sky) 0%,#4fb1dd 45%,var(--blue-deep) 100%)}
.products-title{top:2038px;color:var(--white);font-size:26px}
.product-card{top:2105px;width:224px;height:293px;background:var(--white);box-shadow:0 4px 10px rgba(0,0,0,.35);text-align:center}
.product-pin{position:absolute;left:102px;top:-10px;width:20px;height:20px;border-radius:50%;background:#888;border:3px solid #ccc}
.product-photo{height:181px}
.product-name{margin-top:12px;font-size:10px;color:var(--blue)}
.product-text{margin:10px 22px 0;font-size:10px;line-height:14px;font-weight:700;color:#333}
.product-btn{position:absolute;left:62px;bottom:-14px;width:100px;height:25px;line-height:25px;font-size:9.5px;background:#3b7f9a}
.tone-g{background:linear-gradient(135deg,#f2e9e0,#8ac3e0 60%,#f07fa6)}
.tone-h{background:linear-gradient(135deg,#e9f4f8,#f6d545 55%,#46b6e0)}
.tone-i{background:linear-gradient(135deg,#fbe8f0,#ef7fb2 55%,#f5d44a)}
.arrow{top:2226px;width:50px;height:50px;border-radius:50%;border:2px solid var(--white)}

/* blogs */
.blogs-title{top:2530px;color:#3a8fb0;font-size:26px}
.blog{width:330px;text-align:center}
.blog-photo{width:246px;height:143px;margin:0 auto;border:5px solid var(--white);box-shadow:0 3px 9px rgba(0,0,0,.3)}
.blog-name{margin-top:12px;font-size:10px;color:var(--teal)}
.blog-text{margin-top:4px;font-size:10px;line-height:14px;color:#444}
.blog-more{display:inline-block;margin-top:8px;font-size:9.5px;color:var(--teal);border-bottom:1px solid var(--teal)}
.tone-j{background:linear-gradient(135deg,#efe7e0,#b78a6e)}
.tone-k{background:linear-gradient(135deg,#e8e0d6,#d89548 60%,#b87a3c)}
.see-more{left:536px;top:2865px;width:128px;height:32px;line-height:32px;text-align:center;color:var(--white);background:var(--blue);font-size:11px}

/* footer */
.site-footer{left:0;top:2995px;width:1200px;height:313px;background:linear-gradient(90deg,var(--footer-a) 0%,#0c3550 50%,var(--footer-b) 100%);color:#cfd9df}
.footer-col{top:64px}
.footer-col h4{font-size:13px;font-weight:400;color:var(--white);margin-bottom:9px}
.footer-col ul{list-style:none;font-size:10.5px;line-height:24.6px}
.footer-contact{left:838px;top:62px;font-size:10.5px;line-height:14px;color:var(--white)}
.contact-mark{width:46px;height:46px;border-radius:50%;background:#8d9aa3;margin-left:8px;margin-bottom:16px}
.contact-row{display:flex;gap:10px;align-items:flex-start;margin-bottom:12px}
.bottom-bar{left:0;top:3308px;width:1200px;height:44px;background:#151a1d;color:#bbb;font-size:10px}
.copyright{position:absolute;left:178px;top:15px}
.follow{position:absolute;left:800px;top:9px;display:flex;align-items:center;gap:8px}
.social{width:24px;height:24px;border-radius:50%;border:1px solid #ccc}
</style>
</head>
<body>

<header class="site-header">
  <div class="abs brand-rule"></div>
  <div class="abs brand"><span class="brand-dot"></span><span class="brand-name">Little Burrow</span></div>
  <div class="abs info-box info-address">
    <svg width="14" height="18" viewBox="0 0 14 18"><path d="M7 0a7 7 0 0 0-7 7c0 5 7 11 7 11s7-6 7-11a7 7 0 0 0-7-7zm0 10a3 3 0 1 1 0-6 3 3 0 0 1 0 6z" fill="#fff"/></svg>
    <span>14 Alder Lane,<br>Little Burrow.</span>
  </div>
  <div class="abs info-box info-call">
    <svg width="16" height="16" viewBox="0 0 16 16"><path d="M3 1l3 3-2 2a9 9 0 0 0 6 6l2-2 3 3-2 2C7 15 1 9 1 3z" fill="#fff"/></svg>
    <span>Call Us Now<br><strong>555-014-220</strong></span>
  </div>
</header>

<nav class="abs main-nav">
  <ul class="nav-links">
    <li>HOME</li><li>ABOUT US</li><li>OUR SERVICES</li><li>FUTURE PRODUCT</li><li>BLOG</li><li>TESTIMONIALS</li><li>CONTACT US</li>
  </ul>
  <div class="nav-search">Search ......<span></span></div>
</nav>

<section class="abs hero" role="img" aria-label="Photo of a smiling baby in a pink top playing with colourful toy blocks"></section>
<div class="abs hero-panel">
  <p class="hero-kicker">Text of the printing and type setting</p>
  <h1 class="hero-title">LOREM IPSUM IS SIMPLY</h1>
  <a class="hero-btn">READ MORE &#10141;</a>
</div>

<h2 class="abs welcome-title">Welcome to my site</h2>
<p class="abs welcome-text">Lorem Ipsum is simply dummy text of the printing and typesetting industry. Lorem Ipsum has been the industry's standard dummy text ever since the 1500s, when an unknown printer took a galley of type and scrambled it to make a type specimen book. It has sur typesetting industry. Lorem Ipsum has been the 1500s, when an unknown printer took.a</p>
<a class="abs pill-btn welcome-btn">READ MORE</a>

<h2 class="abs section-title services-title">OUR <em>SERVICES</em></h2>
<p class="abs services-sub">Lorem Ipsum is simply dummy text of the printing and type setting industry.</p>

<div class="abs service" style="left:105px;top:1126px"><div class="service-photo tone-a" role="img" aria-label="Photo of a mother playing with her toddler"></div><p class="service-name">LOREM IPSUM SIMPLY DUMMY</p><p class="service-text">Contrary to popular belief,<br>Lorem Ipsum is not.</p><a class="service-more">READ MORE</a></div>
<div class="abs service" style="left:434px;top:1126px"><div class="service-photo tone-b" role="img" aria-label="Photo of a mother and child wearing toy glasses"></div><p class="service-name">LOREM IPSUM SIMPLY DUMMY</p><p class="service-text">Contrary to popular belief,<br>Lorem Ipsum is not.</p><a class="service-more">READ MORE</a></div>
<div class="abs service" style="left:760px;top:1126px"><div class="service-photo tone-c" role="img" aria-label="Photo of a toddler with a teddy bear and toy stethoscope"></div><p class="service-name">LOREM IPSUM SIMPLY DUMMY</p><p class="service-text">Contrary to popular belief,<br>Lorem Ipsum is not.</p><a class="service-more">READ MORE</a></div>
<div class="abs service" style="left:105px;top:1524px"><div class="service-photo tone-d" role="img" aria-label="Photo of a baby sitting next to a plush toy dog"></div><p class="service-name">LOREM IPSUM SIMPLY DUMMY</p><p class="service-text">Contrary to popular belief,<br>Lorem Ipsum is not.</p><a class="service-more">READ MORE</a></div>
<div class="abs service" style="left:434px;top:1524px"><div class="service-photo tone-e" role="img" aria-label="Photo of a toddler building with wooden blocks"></div><p class="service-name">LOREM IPSUM SIMPLY DUMMY</p><p class="service-text">Contrary to popular belief,<br>Lorem Ipsum is not.</p><a class="service-more">READ MORE</a></div>
<div class="abs service" style="left:760px;top:1524px"><div class="service-photo tone-f" role="img" aria-label="Photo of a mother playing with her baby on the floor"></div><p class="service-name">LOREM IPSUM SIMPLY DUMMY</p><p class="service-text">Contrary to popular belief,<br>Lorem Ipsum is not.</p><a class="service-more">READ MORE</a></div>

<section class="abs products"></section>
<h2 class="abs section-title products-title">FUTURE PRODUCT</h2>
<svg class="abs arrow" style="left:98px" viewBox="0 0 50 50"><path d="M29 15 19 25l10 10" fill="none" stroke="#fff" stroke-width="3"/></svg>
<svg class="abs arrow" style="left:1050px" viewBox="0 0 50 50"><path d="M21 15l10 10-10 10" fill="none" stroke="#fff" stroke-width="3"/></svg>

<article class="abs product-card" style="left:215px"><span class="product-pin"></span><div class="product-photo tone-g" role="img" aria-label="Photo of baby bath bottles and toys"></div><p class="product-name">LOREM IPSUM</p><p class="product-text">Consectetur adipiscing elit, sed do eiusmod tempor incididunt ut labore et dolore</p><a class="pill-btn product-btn">READ MORE</a></article>
<article class="abs product-card" style="left:489px"><span class="product-pin"></span><div class="product-photo tone-h" role="img" aria-label="Photo of folded baby towels and a rubber duck"></div><p class="product-name">LOREM IPSUM</p><p class="product-text">Consectetur adipiscing elit, sed do eiusmod tempor incididunt ut labore et dolore</p><a class="pill-btn product-btn">READ MORE</a></article>
<article class="abs product-card" style="left:762px"><span class="product-pin"></span><div class="product-photo tone-i" role="img" aria-label="Photo of pink baby towels and bath toys"></div><p class="product-name">LOREM IPSUM</p><p class="product-text">Consectetur adipiscing elit, sed do eiusmod tempor incididunt ut labore et dolore</p><a class="pill-btn product-btn">READ MORE</a></article>

<h2 class="abs section-title blogs-title">BLOGS</h2>
<article class="abs blog" style="left:249px;top:2604px"><div class="blog-photo tone-j" role="img" aria-label="Photo of a mother and baby playing on the floor"></div><p class="blog-name">LOREM IPSUM DOLOR SIT AMETCON</p><p class="blog-text">Lorem ipsum dolor sit amet, consectetur adipiscing<br>elit, sed do eiusmod tempor incididunt</p><a class="blog-more">MORE</a></article>
<article class="abs blog" style="left:622px;top:2604px"><div class="blog-photo tone-k" role="img" aria-label="Photo of a toddler in a knitted hat sitting in a cardboard box"></div><p class="blog-name">LOREM IPSUM DOLOR SIT AMETCON</p><p class="blog-text">Lorem ipsum dolor sit amet, consectetur adipiscing<br>elit, sed do eiusmod tempor incididunt</p><a class="blog-more">MORE</a></article>
<a class="abs see-more">SEE MORE</a>

<footer class="abs site-footer">
  <div class="abs footer-col" style="left:161px"><h4>QUICK LINK</h4><ul><li>Home</li><li>About us</li><li>Our Service</li><li>Future Product</li><li>Bolg</li><li>Testmonials</li><li>Contact us</li></ul></div>
  <div class="abs footer-col" style="left:389px"><h4>OUR SERVICES</h4><ul><li>Consectetur</li><li>Adipiscing elit</li><li>Sed do eiusmod</li><li>Tempor</li><li>Incididunt</li><li>Eiusmod</li><li>Incididunt</li></ul></div>
  <div class="abs footer-col" style="left:617px"><h4>OTHER LINK</h4><ul><li>Lorem ipsum</li><li>Dolor</li><li>Sit amet</li><li>Consectetur</li><li>Adipiscing</li><li>Elit, sed</li></ul></div>
  <div class="abs footer-contact">
    <div class="contact-mark"></div>
    <div class="contact-row"><svg width="12" height="15" viewBox="0 0 14 18"><path d="M7 0a7 7 0 0 0-7 7c0 5 7 11 7 11s7-6 7-11a7 7 0 0 0-7-7zm0 10a3 3 0 1 1 0-6 3 3 0 0 1 0 6z" fill="#fff"/></svg><span>14 Alder Lane<br>Little Burrow, Lorem ipsum 21</span></div>
    <div class="contact-row"><svg width="14" height="11" viewBox="0 0 14 11"><rect x=".5" y=".5" width="13" height="10" fill="none" stroke="#fff"/><path d="M.5.5 7 6l6.5-5.5" fill="none" stroke="#fff"/></svg><span>hello@littleburrow.com</span></div>
    <div class="contact-row"><svg width="13" height="13" viewBox="0 0 16 16"><path d="M3 1l3 3-2 2a9 9 0 0 0 6 6l2-2 3 3-2 2C7 15 1 9 1 3z" fill="#fff"/></svg><span>555-014-330</span></div>
  </div>
</footer>
<div class="abs bottom-bar">
  <span class="copyright">&copy; 2017 Little Burrow. All Rights Reserved.</span>
  <div class="follow"><span>Follow us :</span><span class="social"></span><span class="social"></span><span class="social"></span><span class="social"></span><span class="social"></span></div>
</div>

</body>
</html>
```